New Company Business Card design

Looking for a corporate looking business card utilising my new logo design - the logo i would like embossed as one option and flat as another - simplistic but stylish - less is more - we are an import export business launching into the market - i would like a couple of options as main background - Grey or Black

```html
<!DOCTYPE html>
<html lang="en">
<head>
<meta charset="utf-8">
<title>Meridian Trade Partners – Business Card</title>
<link rel="stylesheet" href="https://fonts.googleapis.com/css2?family=PT+Sans:wght@400;700&display=swap">
<style>
  :root {
    --stage: #031a29;
    --card: #ffffff;
    --brand-blue: #0f76bc;
    --text-grey: #55575a;
  }
  html, body {
    margin: 0;
    padding: 0;
    width: 1200px;
    height: 1200px;
    overflow: hidden;
    background: var(--stage);
    font-family: "PT Sans", sans-serif;
  }
  .card {
    position: absolute;
    width: 744px;
    height: 425px;
    background: var(--card);
    border-radius: 45px;
    overflow: hidden;
  }
  .card--front { left: 112px; top: 109px; }
  .card--back  { left: 344px; top: 666px; }

  .front-panel {
    position: absolute;
    left: 0;
    top: 0;
  }
  .contact {
    position: absolute;
    left: 298px;
    top: 122px;
    color: var(--text-grey);
    font-size: 22px;
    line-height: 29px;
  }
  .contact__name {
    margin: 0;
    color: var(--brand-blue);
    font-size: 35px;
    font-weight: 700;
    line-height: 38px;
  }
  .contact__role { margin: 0 0 33px; }
  .contact__lines { margin: 0 0 26px; }
  .contact__address { margin: 0; }

  .brand {
    position: absolute;
    left: 0;
    right: 0;
    top: 0;
    bottom: 0;
    display: flex;
    align-items: center;
    justify-content: center;
    gap: 16px;
  }
  .brand__dot {
    width: 34px;
    height: 34px;
    border-radius: 50%;
    background: var(--brand-blue);
  }
  .brand__name {
    color: var(--brand-blue);
    font-size: 32px;
    font-weight: 700;
    letter-spacing: 2px;
    text-transform: uppercase;
  }
</style>
</head>
<body>
  <section class="card card--front">
    <svg class="front-panel" width="744" height="425" viewBox="0 0 744 425" aria-hidden="true">
      <path d="M0 0 H196 Q30 200 188 425 H0 Z" fill="var(--brand-blue)"/>
    </svg>
    <div class="contact">
      <h1 class="contact__name">MARCO ELLIS</h1>
      <p class="contact__role">Director</p>
      <p class="contact__lines">
        +63 917 555 0142<br>
        marco@meridiantradepartners.com<br>
        www.meridiantradepartners.com
      </p>
      <p class="contact__address">
        Dummy Street, Dummy City<br>
        Dummy Country
      </p>
    </div>
  </section>

  <section class="card card--back">
    <div class="brand">
      <span class="brand__dot" aria-hidden="true"></span>
      <span class="brand__name">Meridian Trade Partners</span>
    </div>
  </section>
</body>
</html>
```